Female Vocalist with/Big Band Concert Marketing Package

Description

We would like to promote our Big Band Concert with a Nationally well known female Vocalist. She won the TV competition Lysfangst being Norways best artist of 2012 : http://www.kvelden-eksempel.no/scene/artikkel.php?artid=48213907

Size requirements :
Poster : A2 and A3
Flyer : 9x14 cm
Newspaper ad : Module 12B : 34 x 80 mm

Delivery file format :
PDFs in CMYK ready for printing
Must be editable in Illustrator CS6

Headlines :
Lene Holvik - main headline
m/Fjordby Jazzlag - big band sharing the act
Storbandaften - theme of this evening

Concert Dates, Venues and Web adresses :
27.april - Moldvik Musikkhall - www.moldvik-musikkhall.no
28.april - Brekkeli Scenehus - www.brekkeli-scenehus.no

Press Pictures and Graphics of artist and band :
May be used or not used according to design

Venue Logos :
There shall be a logo for each venue

Ticket sales logos :
There shall be a logo for each ticket sales office

Sponsors :
There must be a free field with room for sponsor logos

Link to graphics and logos :
https://www.fildeling-eksempel.net/sh/q4wnzrak8dlpx2y/kpTR3mvH9d

Industry/Entity Type

Tv

```html
<!DOCTYPE html>
<html lang="no">
<head>
<meta charset="utf-8">
<title>Lene Holvik &amp; Fjordby Jazzlag – Storbandaften</title>
<link href="https://fonts.googleapis.com/css2?family=Cinzel:wght@400;600&family=Pinyon+Script&family=Open+Sans:wght@400;600&display=swap" rel="stylesheet">
<style>
  :root {
    --cream: #f7f3c8;
    --cream-soft: #eef0d2;
    --plum: #4b3f5f;
    --navy: #1f2347;
    --teal: #1b8fb3;
    --band-left: rgba(60, 140, 200, 0.78);
    --band-right: rgba(90, 205, 215, 0.78);
    --photo-dark: #3b2a2c;
    --photo-mid: #8b6a5c;
    --white: #ffffff;
  }
  * { margin: 0; padding: 0; box-sizing: border-box; }
  html, body { width: 1200px; height: 791px; overflow: hidden; }
  body { background: var(--cream); font-family: "Cinzel", serif; }

  .poster {
    position: relative;
    width: 1200px;
    height: 791px;
    overflow: hidden;
    background:
      radial-gradient(circle at 1080px 330px, rgba(255,255,240,0.7) 0 90px, transparent 92px),
      radial-gradient(circle at 1130px 110px, rgba(255,255,235,0.6) 0 70px, transparent 72px),
      radial-gradient(circle at 860px 80px, rgba(255,255,235,0.5) 0 60px, transparent 62px),
      linear-gradient(100deg, var(--cream-soft) 40%, var(--cream) 100%);
  }

  .artist-photo {
    position: absolute;
    left: 0; top: 0;
    width: 820px; height: 791px;
    background:
      linear-gradient(90deg, rgba(247,243,200,0) 55%, var(--cream-soft) 100%),
      linear-gradient(180deg, var(--photo-dark) 0%, var(--photo-mid) 45%, #a7886f 100%);
  }

  .headline {
    position: absolute;
    right: 33px;
    text-align: right;
    color: var(--plum);
    font-family: "Cinzel", serif;
    font-weight: 600;
    line-height: 1;
  }
  .headline--artist { top: 62px; font-size: 74px; letter-spacing: 1px; }
  .headline--band { top: 180px; font-size: 42px; }
  .headline--band .amp {
    font-family: "Pinyon Script", cursive;
    color: var(--teal);
    font-weight: 400;
    font-size: 60px;
    margin: 0 -6px;
    position: relative;
    top: -18px;
  }

  .theme {
    position: absolute;
    right: 25px;
    top: 270px;
    font-family: "Pinyon Script", cursive;
    font-size: 138px;
    color: var(--teal);
    line-height: 1.2;
  }

  .venue-band {
    position: absolute;
    left: 0; top: 549px;
    width: 1200px; height: 161px;
    background: linear-gradient(90deg, var(--band-left), var(--band-right));
  }
  .venue-band .divider {
    position: absolute;
    left: 701px; top: 18px;
    width: 2px; height: 125px;
    background: var(--navy);
  }

  .venue {
    position: absolute;
    top: 22px;
    color: var(--navy);
  }
  .venue--first { left: 224px; }
  .venue--second { left: 755px; }
  .venue__date {
    font-size: 24px;
    font-weight: 600;
    white-space: nowrap;
  }
  .venue__url {
    margin-top: 8px;
    font-size: 20px;
    font-weight: 600;
    white-space: nowrap;
  }
  .venue__logos {
    margin-top: 12px;
    display: flex;
    align-items: center;
    gap: 26px;
  }
  .logo-name {
    display: flex;
    align-items: center;
    gap: 8px;
    font-family: "Open Sans", sans-serif;
    font-size: 19px;
    font-weight: 600;
    color: var(--navy);
    white-space: nowrap;
  }
  .logo-name .mark {
    width: 22px; height: 22px;
    background: var(--navy);
  }
  .logo-name .mark--round { border-radius: 50%; }

  .sponsors {
    position: absolute;
    top: 742px;
    left: 0;
    width: 1200px;
  }
  .sponsor {
    position: absolute;
    display: flex;
    align-items: center;
    gap: 8px;
    font-family: "Open Sans", sans-serif;
    font-size: 13px;
    color: var(--white);
  }
  .sponsor .dot {
    width: 26px; height: 26px;
    border-radius: 50%;
    background: #fffbe0;
  }
</style>
</head>
<body>
<main class="poster">
  <div class="artist-photo" role="img" aria-label="Press photo of the vocalist with long brown hair, gazing upward in warm light"></div>

  <h1 class="headline headline--artist">Lene Holvik</h1>
  <h2 class="headline headline--band">Fjordby<span class="amp">&amp;</span>Jazzlag</h2>
  <p class="theme">Storbandaften</p>

  <section class="venue-band">
    <div class="venue venue--first">
      <p class="venue__date">27.april - Moldvik Musikkhall</p>
      <p class="venue__url">www.moldvik-musikkhall.no</p>
      <div class="venue__logos">
        <span class="logo-name">Moldvik Musikkhall</span>
        <span class="logo-name"><span class="mark"></span>Billettkassen</span>
      </div>
    </div>
    <div class="divider"></div>
    <div class="venue venue--second">
      <p class="venue__date">28.april - Brekkeli Scenehus</p>
      <p class="venue__url">www.brekkeli-scenehus.no</p>
      <div class="venue__logos">
        <span class="logo-name"><span class="mark mark--round"></span>Billettsentralen</span>
      </div>
    </div>
  </section>

  <section class="sponsors">
    <div class="sponsor" style="left:203px"><span class="dot"></span>sponsor logos</div>
    <div class="sponsor" style="left:358px"><span class="dot"></span>sponsor logos</div>
    <div class="sponsor" style="left:507px"><span class="dot"></span>sponsor logos</div>
    <div class="sponsor" style="left:660px"><span class="dot"></span>sponsor logos</div>
  </section>
</main>
</body>
</html>
```